Lantern Pier Entertainment | Business Card & Logo

We are looking for a business card with a Logo.
It’s a brand new business and we are looking for an elegant design.
The business service categories are:
Photo Booth
Photography
Events Planning
Marcus Halloway
0471259038
0386217493
info@lanternpierentertainment.com.au
www.lanternpierentertainment.com.au
Target Market(s)
Corporate, Photo Booth, Photography and event planning
Industry/Entity Type
Photo Booth, Photography and event planning
Contact Information for Business Card
Marcus Halloway | 0471259038 | 0386217493 | info@lanternpierentertainment.com.au | www.lanternpierentertainment.com.au

```html
<!DOCTYPE html>
<html lang="en">
<head>
<meta charset="UTF-8">
<title>Lantern Pier Entertainment | Business Card</title>
<link href="https://fonts.googleapis.com/css2?family=Montserrat:wght@600&family=Open+Sans:wght@400&display=swap" rel="stylesheet">
<style>
  :root {
    --backdrop: #2b2b2d;
    --card: #141414;
    --edge: #e0846c;
    --crimson: #d3354b;
    --gold: #d8b45c;
    --body-text: #cfcfcf;
  }
  * { margin: 0; padding: 0; box-sizing: border-box; }
  html, body {
    width: 1200px;
    height: 875px;
    overflow: hidden;
    background: var(--backdrop);
  }
  .sheet {
    width: 1200px;
    height: 875px;
    display: flex;
    align-items: center;
    justify-content: center;
    gap: 40px;
  }
  .card {
    width: 540px;
    height: 310px;
    background: var(--card);
    border: 1.5px solid var(--edge);
    border-radius: 18px;
    position: relative;
    overflow: hidden;
  }
  .brand {
    display: flex;
    align-items: center;
    gap: 14px;
    font-family: "Montserrat", sans-serif;
    font-weight: 600;
    color: var(--crimson);
  }
  .brand-dot {
    border-radius: 50%;
    background: var(--crimson);
    flex: none;
  }
  .brand-name { line-height: 1.15; }
  .brand-name span { display: block; }

  /* Front */
  .card-front {
    display: flex;
    align-items: center;
    justify-content: center;
  }
  .card-front .brand-dot { width: 44px; height: 44px; }
  .card-front .brand-name .line-main { font-size: 34px; }
  .card-front .brand-name .line-sub { font-size: 18px; letter-spacing: 3px; }

  /* Back */
  .card-back .brand {
    position: absolute;
    left: 34px;
    top: 128px;
    gap: 10px;
  }
  .card-back .brand-dot { width: 26px; height: 26px; }
  .card-back .brand-name .line-main { font-size: 21px; }
  .card-back .brand-name .line-sub { font-size: 11px; letter-spacing: 2px; }

  .contact {
    position: absolute;
    left: 262px;
    top: 78px;
    width: 260px;
  }
  .contact-name {
    font-family: "Montserrat", sans-serif;
    font-weight: 600;
    font-size: 23px;
    color: var(--crimson);
  }
  .contact-rule {
    width: 62px;
    height: 2px;
    background: var(--gold);
    margin: 8px 0 14px;
  }
  .contact-list { list-style: none; }
  .contact-list li {
    display: flex;
    align-items: center;
    gap: 9px;
    font-family: "Open Sans", sans-serif;
    font-size: 11.5px;
    color: var(--body-text);
    margin-bottom: 9px;
    white-space: nowrap;
  }
  .contact-icon { width: 12px; height: 12px; flex: none; }
</style>
</head>
<body>
<main class="sheet">

  <section class="card card-front" aria-label="Business card front">
    <div class="brand">
      <div class="brand-dot"></div>
      <div class="brand-name">
        <span class="line-main">Lantern Pier</span>
        <span class="line-sub">Entertainment</span>
      </div>
    </div>
  </section>

  <section class="card card-back" aria-label="Business card back">
    <div class="brand">
      <div class="brand-dot"></div>
      <div class="brand-name">
        <span class="line-main">Lantern Pier</span>
        <span class="line-sub">Entertainment</span>
      </div>
    </div>

    <div class="contact">
      <h1 class="contact-name">Marcus Halloway</h1>
      <div class="contact-rule"></div>
      <ul class="contact-list">
        <li>
          <svg class="contact-icon" viewBox="0 0 24 24" aria-hidden="true"><path fill="#d3354b" d="M6.6 10.8a15.1 15.1 0 0 0 6.6 6.6l2.2-2.2a1 1 0 0 1 1-.25 11.4 11.4 0 0 0 3.6.57 1 1 0 0 1 1 1V20a1 1 0 0 1-1 1A17 17 0 0 1 3 4a1 1 0 0 1 1-1h3.5a1 1 0 0 1 1 1c0 1.25.2 2.45.57 3.57a1 1 0 0 1-.25 1z"/></svg>
          (047) 125-9038
        </li>
        <li>
          <svg class="contact-icon" viewBox="0 0 24 24" aria-hidden="true"><rect x="6" y="2" width="12" height="20" rx="2" fill="none" stroke="#d3354b" stroke-width="2.4"/><circle cx="12" cy="18" r="1.4" fill="#d3354b"/></svg>
          (038) 621-7493
        </li>
        <li>
          <svg class="contact-icon" viewBox="0 0 24 24" aria-hidden="true"><rect x="2" y="5" width="20" height="14" rx="1.5" fill="#d3354b"/><path d="M3 6l9 7 9-7" fill="none" stroke="#141414" stroke-width="1.8"/></svg>
          info@lanternpierentertainment.com.au
        </li>
        <li>
          <svg class="contact-icon" viewBox="0 0 24 24" aria-hidden="true"><circle cx="12" cy="12" r="9.5" fill="none" stroke="#d3354b" stroke-width="2.2"/><ellipse cx="12" cy="12" rx="4" ry="9.5" fill="none" stroke="#d3354b" stroke-width="1.6"/><path d="M2.5 12h19" stroke="#d3354b" stroke-width="1.6"/></svg>
          lanternpierentertainment.com.au
        </li>
      </ul>
    </div>
  </section>

</main>
</body>
</html>
```